"Uncle's Old Pony" Bookcover 170501

We need a book cover for print edition of the title, "Uncle's Old Pony". The book is about the life of a man and that of his last dog, told from the perspective of his son. The book is a mix of highly improbable situations and a son's remembrance of his father. We've attached pictures of both the man and the dog, however, they do not have to be used, if it doesn't add to the design. It does provide an idea of what the subjects looked like. The author's name is Rob T. Vessard. The publisher will be Quiet Heron Publishers. One book size template uploaded. NOTE: Designer credit will be included in the published work.

Target Market(s)

People who like non-fiction strange family and dog stories

Font styles to use
Serif
Sans Serif

Colors

Designer to choose colors to be used in the design.

Requirements
Must have
• A means of communicating a story about two lifetimes, the man and the dog. Full cover, front, spine and back.
Nice to have
• Man and Dog get equal billing, something that indicates a lifetime of events
Should not have
• A mere collage of the uploaded pics. Those can be used, but don't make it as simple as a photo album.

```html
<!DOCTYPE html>
<html lang="en">
<head>
<meta charset="utf-8">
<title>Uncle's Old Pony — Full Cover</title>
<link rel="stylesheet" href="https://fonts.googleapis.com/css2?family=Playfair+Display:wght@400;700&family=Marcellus&family=Tinos&display=swap">
<style>
  :root {
    --page: #ffffff;
    --sky-top: #3f6a6c;
    --sky-mid: #7d9a86;
    --glow: #f2c46a;
    --horizon: #f6a94a;
    --ridge: #2b3a33;
    --field: #161a14;
    --panel-top: #f3c35c;
    --panel-bottom: rgba(250, 226, 160, 0.15);
    --ink: #1e1e1a;
    --title-green: #8cc7a0;
    --title-cream: #f4e2a8;
    --author-gold: #d9c68c;
    --spine-ink: #1c2320;
    --light: #f6efd8;
  }
  * { box-sizing: border-box; margin: 0; padding: 0; }
  html, body {
    width: 1200px; height: 1200px; overflow: hidden;
    background: var(--page);
  }
  .cover {
    position: absolute; left: 230px; top: 294px;
    width: 771px; height: 555px; overflow: hidden;
  }
  .cover-scene { position: absolute; inset: 0; }
  .genre {
    position: absolute; left: 23px; top: 30px;
    font: 9px "Tinos", serif; color: var(--light); letter-spacing: 0.3px;
  }
  .back-panel {
    position: absolute; left: 21px; top: 55px; width: 324px; height: 337px;
    background: linear-gradient(to bottom, var(--panel-top) 0%, rgba(248,214,120,0.85) 45%, var(--panel-bottom) 100%);
    border-top: 1px solid rgba(255,240,200,0.8);
    border-left: 1px solid rgba(255,240,200,0.5);
    border-right: 1px solid rgba(255,240,200,0.5);
    padding: 10px 14px 0 15px; color: var(--ink);
  }
  .back-heading {
    font: 19px/24px "Marcellus", serif; text-align: center; margin-bottom: 6px;
  }
  .back-blurb, .author-bio {
    font: 11.1px/18px "Tinos", serif;
  }
  .author-bio { margin-top: 12px; margin-left: -2px; }
  .isbn-box {
    position: absolute; left: 238px; top: 471px; width: 108px; height: 62px;
    background: #ffffff;
  }
  .publisher-back {
    position: absolute; left: 12px; top: 478px; width: 80px;
    display: flex; flex-direction: column; align-items: center; gap: 6px;
    font: 10px/11px "Tinos", serif; color: var(--light); text-align: center;
    text-transform: uppercase;
  }
  .mark-dot { width: 26px; height: 26px; border-radius: 50%; background: var(--glow); }
  .spine {
    position: absolute; left: 367px; top: 26px; width: 34px; height: 420px;
    writing-mode: vertical-rl; display: flex; align-items: flex-start;
  }
  .spine-title {
    font: 700 27px/34px "Playfair Display", serif; color: var(--spine-ink);
    letter-spacing: 0.5px; text-transform: uppercase;
  }
  .spine-author {
    position: absolute; top: 294px; left: 8px;
    font: 12px/18px "Tinos", serif; color: var(--spine-ink);
  }
  .spine-dot {
    position: absolute; left: 376px; top: 515px; width: 16px; height: 16px;
    border-radius: 50%; background: var(--glow);
  }
  .front-title {
    position: absolute; left: 424px; top: 20px;
    font: 400 84px/98px "Playfair Display", serif; text-transform: uppercase;
    letter-spacing: -1px;
  }
  .front-title .line { display: block; }
  .front-title .line-1 { color: var(--title-green); }
  .front-title .line-2, .front-title .line-3 { color: var(--title-cream); }
  .front-author {
    position: absolute; left: 556px; top: 502px;
    font: 31px/36px "Marcellus", serif; color: var(--author-gold);
  }
</style>
</head>
<body>
  <section class="cover">
    <svg class="cover-scene" role="img" aria-label="Photograph: a man and his dog walking across a dark field toward a forested ridge at sunset" width="771" height="555" viewBox="0 0 771 555">
      <defs>
        <linearGradient id="sky" x1="0" y1="0" x2="0" y2="1">
          <stop offset="0" stop-color="var(--sky-top)"/>
          <stop offset="0.4" stop-color="var(--sky-mid)"/>
          <stop offset="0.68" stop-color="var(--glow)"/>
          <stop offset="0.77" stop-color="var(--horizon)"/>
          <stop offset="0.8" stop-color="var(--ridge)"/>
          <stop offset="1" stop-color="var(--field)"/>
        </linearGradient>
      </defs>
      <rect width="771" height="555" fill="url(#sky)"/>
    </svg>

    <p class="genre">BIOGRAPHY</p>

    <article class="back-panel">
      <h2 class="back-heading">A Man’s Great Love for his<br>Faithful Companion</h2>
      <p class="back-blurb">The book is about the life of a man and that of his last dog, told from the perspective of his son. The book is a mix of highly improbable situations and a son's remembrance of his father. The book is about the life of a man and that of his last dog, told from the perspective of his son. The book is a mix of highly improbable situations and a son's remembrance of his father.</p>
      <p class="author-bio">Rob T. Vessard was born in Someplace, California. He is married with three children. He realized at an early age his love for writing, and has written short stories and poetry for both adults and children. He is an avid adventurer, who has ventured into some of the most dangerous areas in the world, with only a knife and a backpack.</p>
    </article>

    <div class="isbn-box"></div>

    <div class="publisher-back">
      <span class="mark-dot"></span>
      <span>Quiet Heron<br>Publishers</span>
    </div>

    <div class="spine">
      <span class="spine-title">Uncle’s Old Pony</span>
      <span class="spine-author">Rob T. Vessard</span>
    </div>
    <span class="spine-dot"></span>

    <h1 class="front-title">
      <span class="line line-1">Uncle’s</span>
      <span class="line line-2">Old</span>
      <span class="line line-3">Pony</span>
    </h1>
    <p class="front-author">Rob T. Vessard</p>
  </section>
</body>
</html>
```